Plumvex Healthy Juices paper cups

We need a packaging design on paper cups of fruit shakes /juices we are selling. We want to communicate sexy body, health and refreshing. We wanted to stick to white and red color only but we are open to all suggestions...however, we wanted red to be dominating color.

I attached a sample but I believe that there is something more than this glass. I hope to see better, much better than this. Though we can use this cup but some finishing touch or better design with the red stripes will be ok.
Updates

I now included the previous packaging design but we want to communicate sexy, health and refreshing drink. I also downloaded our cart / kiosk for your guide. Thank you.

Hi to all designers, good day. I added jiva brisk to become your inspirations in designing our plumvex cups. Many thanks!

Reason: To attract more designs and give time to designers to conceptualise.

Hi Designers, i would like to apologise sincerely but the business is no longer viable due to management decision. For that reason, I am no longer continuing this venture. Thank you for your understanding.

Target Market(s)

male and female who are health conscious

Industry/Entity Type

Health

Colors
eb1f27
ffffff

Requirements
Must have
• red and white color primary colors

```html
<!DOCTYPE html>
<html lang="en">
<head>
<meta charset="utf-8">
<title>Plumvex Healthy Juices – Cup Wrap</title>
<link href="https://fonts.googleapis.com/css2?family=Fredoka:wght@600&family=PT+Sans+Narrow&display=swap" rel="stylesheet">
<style>
  :root {
    --page: #ffffff;
    --red-base: #c9000b;
    --red-bright: #e10007;
    --red-deep: #8a0008;
    --white: #ffffff;
    --pink-dot: #f29a9a;
  }
  html, body {
    margin: 0;
    padding: 0;
    width: 1200px;
    height: 938px;
    overflow: hidden;
    background: var(--page);
  }
  .cup-wrap {
    position: relative;
    width: 1200px;
    height: 938px;
  }
  .cup-wrap svg { position: absolute; inset: 0; }
  .brand-name {
    font-family: "Fredoka", "Arial Rounded MT Bold", sans-serif;
    font-weight: 600;
    fill: var(--white);
  }
  .fine-print {
    position: absolute;
    left: 922px;
    top: 735px;
    width: 172px;
    margin: 0;
    font-family: "PT Sans Narrow", "Arial Narrow", sans-serif;
    font-size: 10.5px;
    line-height: 1.4;
    color: var(--white);
  }
</style>
</head>
<body>
<main class="cup-wrap">
  <svg width="1200" height="938" viewBox="0 0 1200 938" xmlns="http://www.w3.org/2000/svg">
    <defs>
      <clipPath id="wrap-area">
        <rect x="52" y="62" width="1093" height="810"/>
      </clipPath>
    </defs>

    <g clip-path="url(#wrap-area)">
      <rect class="panel" x="52" y="62" width="1093" height="810" fill="var(--red-base)"/>

      <path class="swoosh" d="M140 62 C100 300 200 560 470 872 L560 872 C300 600 220 330 275 62 Z" fill="var(--red-bright)"/>
      <path class="swoosh" d="M740 62 C780 260 900 430 1145 600 L1145 720 C860 560 700 330 700 62 Z" fill="var(--red-bright)"/>
      <path class="swoosh" d="M850 62 C880 200 980 330 1145 420 L1145 460 C960 380 860 240 830 62 Z" fill="var(--red-bright)" opacity="0.7"/>

      <path class="flow" d="M585 62 L650 62 C640 200 700 330 690 470 C680 600 640 720 660 872 L440 872 C470 760 520 680 560 600 C600 480 560 330 600 200 C610 150 590 100 585 62 Z" fill="var(--white)"/>
      <path class="flow-inner" d="M600 62 L630 62 C620 180 660 260 650 360 L600 330 C610 240 590 150 600 62 Z" fill="var(--red-base)"/>
      <path class="flow-edge" d="M520 150 C470 320 430 520 420 872 L380 872 C400 560 440 330 500 130 Z" fill="var(--pink-dot)" opacity="0.55"/>
      <path class="flow-edge" d="M700 100 C760 330 700 560 680 872 L660 872 C670 600 740 340 690 110 Z" fill="var(--red-deep)" opacity="0.6"/>

      <path class="ribbon" d="M975 62 C1060 230 1040 420 960 600 C910 710 880 790 880 872" fill="none" stroke="var(--white)" stroke-width="16"/>
      <path class="ribbon" d="M960 62 C1010 240 990 420 920 590 C890 670 870 760 860 872" fill="none" stroke="var(--red-deep)" stroke-width="5" opacity="0.7"/>
    </g>

    <!-- brand oval with wordmark and tagline aligned to its long axis -->
    <g class="brand-badge" transform="translate(580 450) rotate(12)">
      <ellipse rx="112" ry="178" fill="var(--white)"/>
      <ellipse rx="100" ry="166" fill="var(--red-base)"/>
      <g transform="rotate(-90)">
        <text class="brand-name" x="-6" y="4" font-size="64" text-anchor="middle">Plumvex</text>
        <text class="brand-name" x="38" y="32" font-size="20" letter-spacing="1" text-anchor="middle">HEALTHY JUICES</text>
      </g>
    </g>

    <!-- flavour badge -->
    <circle cx="540" cy="775" r="68" fill="var(--white)"/>
    <circle cx="540" cy="775" r="61" fill="var(--red-deep)" role="img" aria-label="Banana illustration with Banana flavour label"/>

    <!-- disposal icon -->
    <g class="icon-bin" fill="var(--white)">
      <circle cx="963" cy="810" r="6"/>
      <rect x="957" y="818" width="12" height="34" rx="2"/>
      <path d="M938 830 L952 830 L949 852 L941 852 Z"/>
    </g>

    <!-- recycle icon: three chasing arrows -->
    <g class="icon-recycle">
      <g fill="none" stroke="var(--white)" stroke-width="5" stroke-linecap="round">
        <path d="M1030 813 L1041 833"/>
        <path d="M1042 848 L1017 848"/>
        <path d="M1008 843 L1019 823"/>
      </g>
      <g fill="var(--white)">
        <path d="M1046 842 L1045.4 830.6 L1036.6 835.4 Z"/>
        <path d="M1010 848 L1017 842 L1017 854 Z"/>
        <path d="M1023 815 L1023.4 824.4 L1014.6 819.6 Z"/>
      </g>
    </g>
  </svg>

  <p class="fine-print">Lorem ipsum dolor sit amet, consectetuer adipiscing elit. Aenean commodo ligula eget dolor. Aenean massa.</p>
</main>
</body>
</html>
```